Anzeige in Kongressbüchlein für Zahnarztkongress
Zielgruppe
Die Dienstleistung der Velumbra AG ist die Praxisnarkose. Sprich wir behandeln Patienten vor Ort - z.B. beim Zahnarzt in der Praxis. Wir bringen alles mit. Bei den Patienten handelt es sich um Kinder, Angstpatienten oder beeinträchtigte Patienten. Anzeige ist in DIN A5.
look @ www.velumbra.ch
Aufgabenstellung
Anzeige mit unserem Logo und unseren Farben als Wiedererkennung gestallten. so wenig Text wie möglich - die DL muss klar ersichtlich sein. Aufruf zur Kontaktaufnahme. Evtl.. QR -Code. Evtl. Foto von der Homepage.

```html
<!DOCTYPE html>
<html lang="de">
<head>
<meta charset="utf-8">
<title>Velumbra AG – Praxisanästhesie</title>
<link rel="stylesheet" href="https://fonts.googleapis.com/css2?family=Arimo:wght@400;700&display=swap">
<style>
  :root {
    --green: #7ea31c;
    --grey: #6b6b6d;
    --grey-light: #8a8a8c;
    --bg-top: #f4f5f6;
    --bg-mid: #eceef0;
    --photo-a: #a9c4c6;
    --photo-b: #e6e3de;
  }
  html, body { margin: 0; padding: 0; overflow: hidden; }
  .ad {
    position: relative;
    width: 846px;
    height: 1200px;
    overflow: hidden;
    font-family: "Arimo", Arial, sans-serif;
    background:
      radial-gradient(ellipse 420px 160px at 620px 1120px, rgba(255,255,255,0.9), transparent 70%),
      radial-gradient(ellipse 380px 140px at 180px 980px, rgba(255,255,255,0.8), transparent 70%),
      radial-gradient(ellipse 500px 180px at 700px 200px, rgba(225,228,232,0.7), transparent 70%),
      linear-gradient(180deg, var(--bg-top) 0%, #f7f8f9 40%, var(--bg-mid) 100%);
  }
  .brand {
    position: absolute;
    top: 66px;
    left: 0;
    width: 846px;
    margin: 0;
    text-align: center;
    font-size: 74px;
    line-height: 90px;
    font-weight: 400;
    color: var(--grey);
    letter-spacing: 1px;
  }
  .tagline {
    position: absolute;
    top: 174px;
    left: 0;
    width: 846px;
    margin: 0;
    text-align: center;
    font-size: 28px;
    letter-spacing: 1px;
    color: var(--grey-light);
  }
  .hero {
    position: absolute;
    top: 262px;
    left: 0;
    width: 846px;
    height: 396px;
    box-sizing: border-box;
    border-top: 4px solid var(--green);
    border-bottom: 4px solid var(--green);
    background: linear-gradient(100deg, var(--photo-b) 0%, #d9cbb6 30%, var(--photo-a) 60%, #cfd6d8 100%);
  }
  .content {
    position: absolute;
    top: 718px;
    left: 63px;
    color: var(--grey);
    font-size: 27px;
  }
  .headline { margin: 0 0 34px; }
  .headline strong { color: var(--green); }
  .services {
    list-style: none;
    margin: 0 0 38px;
    padding: 0 0 0 57px;
    color: var(--green);
    font-size: 27px;
    line-height: 33px;
  }
  .services li::before {
    content: "❖";
    display: inline-block;
    width: 38px;
    font-size: 20px;
  }
  .claim { margin: 0 0 34px; font-size: 27.5px; }
  .call { margin: 0; font-size: 27.5px; }
  .contact {
    position: absolute;
    top: 1114px;
    left: 63px;
    font-size: 18.5px;
    line-height: 22px;
    margin: 0;
  }
  .contact .company { color: var(--green); display: block; }
  .contact .lines { color: var(--grey); display: block; }
</style>
</head>
<body>
<div class="ad">
  <h1 class="brand">velumbra</h1>
  <p class="tagline">Narkose direkt in Ihrer Praxis</p>

  <div class="hero" role="img" aria-label="Foto: zwei lächelnde Anästhesistinnen in weissen Shirts mit einem Kind auf der Behandlungsliege, das ein Stofftier mit Stethoskop abhört"></div>

  <section class="content">
    <p class="headline"><strong>Praxisanästhesie</strong> mal anders erleben mit Velumbra.</p>
    <ul class="services">
      <li>Angstpatienten (auch mit Dämmerschlaf)</li>
      <li>Beeinträchtige Patienten</li>
      <li>Kinder</li>
    </ul>
    <p class="claim">Wir kommen gerne zu Ihnen – In Ihre Stadt – in Ihre Praxis</p>
    <p class="call">Rufen Sie uns an – wir freuen uns auf SIE!</p>
  </section>

  <p class="contact">
    <span class="company">Velumbra AG | Lindenweg 42 | CH-4600 Olten</span>
    <span class="lines">fon +41 62 555 01 93 | fax +41 62 555 01 92 | info@velumbra.ch | www.velumbra.ch</span>
  </p>
</div>
</body>
</html>
```